Business Card Design

We are a residential half way house for the addict ,the alcoholic and dual diagnosed in recovery.
i house both men and woman age 18+

Industry/Entity Type

Residential

```html
<!DOCTYPE html>
<html lang="en">
<head>
<meta charset="utf-8">
<title>Harbor Light Sober Living – Business Card</title>
<link rel="stylesheet" href="https://fonts.googleapis.com/css2?family=Lato:wght@300;400;700;900&display=swap">
<style>
  :root {
    --ink: #0b0b0b;
    --paper: #ffffff;
    --lime: #a9cf3a;
    --lime-dark: #8db52a;
    --backdrop: #d9d9d9;
    --text-dark: #141414;
    --text-light: #f4f4f4;
  }
  * { margin: 0; padding: 0; box-sizing: border-box; }
  html, body {
    width: 1200px; height: 926px; overflow: hidden;
    background: var(--backdrop);
    font-family: "Lato", sans-serif;
  }
  .canvas { position: relative; width: 1200px; height: 926px; }

  .card {
    position: absolute; left: 300px; width: 600px; height: 343px;
    overflow: hidden; box-shadow: 0 6px 18px rgba(0,0,0,.18);
  }
  .card-front { top: 60px; background: var(--paper); }
  .card-back { top: 490px; background: var(--ink); }
  .card-shape { position: absolute; inset: 0; }

  .company-name {
    position: absolute; font-weight: 400; letter-spacing: -0.3px; white-space: nowrap;
  }
  .card-front .company-name { left: 118px; top: 40px; font-size: 27px; color: var(--text-dark); }
  .card-back .company-name { right: 40px; top: 210px; font-size: 25px; color: var(--text-light); }

  .owner { position: absolute; left: 36px; top: 142px; }
  .owner-name {
    font-size: 17px; color: var(--text-light); font-weight: 300; letter-spacing: .3px;
  }
  .owner-name strong { font-weight: 700; }
  .owner-role { font-size: 12px; color: var(--lime); margin-top: 2px; }

  .contact-list {
    position: absolute; left: 330px; top: 186px; list-style: none;
    color: var(--text-light); font-size: 15.5px; font-weight: 700; letter-spacing: .2px;
  }
  .contact-list li { display: flex; align-items: center; height: 20px; }
  .contact-icon { width: 13px; height: 12px; margin-right: 9px; flex: none; }

  .address {
    position: absolute; font-weight: 900; font-size: 15px; letter-spacing: 4.2px;
    color: var(--text-dark); white-space: nowrap; text-transform: uppercase;
  }
  .card-front .address { left: 38px; top: 309px; }
  .card-back .address { right: 30px; top: 272px; }
</style>
</head>
<body>
<main class="canvas">

  <section class="card card-front" aria-label="Business card front">
    <svg class="card-shape" viewBox="0 0 600 343" width="600" height="343" aria-hidden="true">
      <path d="M0,125 C250,108 450,140 600,232 L600,343 L0,343 Z" fill="var(--ink)"/>
      <path d="M0,121 C230,104 420,130 560,200" fill="none" stroke="var(--lime)" stroke-width="3"/>
      <rect x="0" y="298" width="600" height="45" fill="var(--lime)"/>
    </svg>

    <h1 class="company-name">Harbor Light Sober Living Inc.</h1>

    <div class="owner">
      <p class="owner-name">DANA <strong>WHITFIELD</strong></p>
      <p class="owner-role">Owner (15 yrs.in recovery)</p>
    </div>

    <ul class="contact-list">
      <li>
        <svg class="contact-icon" viewBox="0 0 13 12" aria-hidden="true"><path d="M1,4 Q6.5,-1 12,4 L10,6 L8.5,4.5 L4.5,4.5 L3,6 Z M3,7 L10,7 L11,11 L2,11 Z" fill="var(--lime)"/></svg>
        (555) 014-0305
      </li>
      <li>
        <svg class="contact-icon" viewBox="0 0 13 12" aria-hidden="true"><path d="M1,4 Q6.5,-1 12,4 L10,6 L8.5,4.5 L4.5,4.5 L3,6 Z M3,7 L10,7 L11,11 L2,11 Z" fill="var(--lime)"/></svg>
        (555) 014-0306
      </li>
      <li>
        <svg class="contact-icon" viewBox="0 0 13 12" aria-hidden="true"><rect x="3" y="0" width="7" height="4" fill="var(--lime)"/><rect x="0" y="5" width="13" height="5" rx="1" fill="var(--lime)"/><rect x="3" y="8" width="7" height="4" fill="var(--lime)"/></svg>
        Fax (555) 014-5536
      </li>
      <li>
        <svg class="contact-icon" viewBox="0 0 13 12" aria-hidden="true"><rect x="0" y="2" width="13" height="9" fill="var(--lime)"/><path d="M0,2 L6.5,7 L13,2" fill="none" stroke="var(--ink)" stroke-width="1.2"/></svg>
        email dwhitfield@example.com
      </li>
    </ul>

    <p class="address">1820 Palmetto Rd. Bay Haven, FLA 34000</p>
  </section>

  <section class="card card-back" aria-label="Business card back">
    <svg class="card-shape" viewBox="0 0 600 343" width="600" height="343" aria-hidden="true">
      <rect x="0" y="255" width="600" height="88" fill="var(--lime)"/>
    </svg>
    <h2 class="company-name">Harbor Light Sober Living Inc.</h2>
    <p class="address">1820 Palmetto Rd. Bay Haven, FLA 34000</p>
  </section>

</main>
</body>
</html>
```